Glintora.ca Website Build For costume embellishment service

Design a website to promote our business.
Costume embellishing services for Artistic Swimming, Dance, Skating, Gymnastics etc.
We add sparkle to costumes using Velmareth and Lustrina crystals to plain costumes that our customers provide. We also sell new costumes already decorated, Lastly we specialize in reimagining costumes to make them look like new.
We would like samples of our work to be displayed in pictures and video.
We need an information about our services page as well as a contact us page. We have a logo for Glintora which is pink. We like a modern aesthetic as well as bright colours. We are hoping to promote our services worldwide but a big push for Canada. We need to convey that we are Canadian. We would like help with writing copy as well.
We currently have a cartwell webpage glintora.ca but would like to shut down the cartwell site as we don't need the payment service. In the new website we will promote payment by PayPal or transfer.
A copy of our logo is attached.

Target Market(s)

Athletes and Dancers under 18 years old and parents

Industry/Entity Type

costume embellishment service

Coding

Coded - Design and coding required

Number of Pages Required

4 page

Font styles to use
Sans Serif
Other font styles liked:
• match to the logo for titles

Colors
E54698
E96AAD
F1A4CE
F9D9EA
FCEFF6

Requirements
Must have
• Photos and video upload capability there will be allot of before and after pictures as well as unclose videos.
Nice to have
• modern look I like the look of this website http://www.brindlecourtstudio.com
Should not have
• not busy looking

```html
<!DOCTYPE html>
<html lang="en">
<head>
<meta charset="utf-8">
<title>Glintora – Contact</title>
<link rel="stylesheet" href="https://fonts.googleapis.com/css2?family=Mulish:wght@300;400;600&display=swap">
<style>
:root{
  --pink:#e54698;
  --pink-soft:#e96aad;
  --pink-deep:#c5258b;
  --ink:#444;
  --muted:#777;
  --line:#cfcfcf;
  --white:#fff;
}
*{box-sizing:border-box;margin:0;padding:0}
html,body{width:1035px;height:1200px;overflow:hidden;background:var(--white)}
body{position:relative;font-family:"Mulish",sans-serif;color:var(--ink)}
.hero{position:absolute;left:0;top:0;width:1035px;height:474px;
  background:linear-gradient(100deg,#c8488f 0%,#b6538f 35%,#8a6a78 55%,#4c4440 75%,#2f2b29 100%)}
.site-header{position:absolute;left:0;top:11px;width:1026px;height:67px;background:var(--pink)}
.brand{position:absolute;left:171px;top:22px;display:flex;align-items:center;gap:6px;color:var(--white);font-size:17px;font-weight:400}
.brand-dot{width:8px;height:8px;border-radius:50%;background:var(--white)}
.main-nav{position:absolute;top:29px;left:0;width:100%;font-size:7.5px}
.main-nav a{position:absolute;color:var(--white);text-decoration:none}
.main-nav a.current{color:#f6c4df}
.hero-title{position:absolute;left:0;width:100%;top:186px;text-align:center;color:var(--white);font-size:23px;font-weight:400;letter-spacing:.5px}
.breadcrumb{position:absolute;left:0;width:100%;top:226px;text-align:center;font-size:7.5px;color:var(--white);letter-spacing:.4px}
.breadcrumb b{font-weight:600;margin-right:6px}
.breadcrumb span{color:#f0dbe6}
.section-title{position:absolute;left:175px;top:527px;font-size:13px;font-weight:400;color:#333}
.info{position:absolute;top:564px;font-size:8.6px;line-height:15px;color:var(--muted);width:160px}
.info strong{font-weight:400;color:#333}
.map{position:absolute;left:175px;top:628px;width:334px;height:215px;background:linear-gradient(120deg,#5f7a58 0%,#6f8a62 40%,#3b5a7c 60%,#2f5275 100%)}
.contact-form{position:absolute;left:526px;top:628px;width:316px}
.field{display:block;width:316px;height:28px;border:1px solid var(--line);font:inherit;font-size:8px;color:var(--muted);padding:0 7px;margin-bottom:9px;background:var(--white);line-height:26px}
.field.message{height:90px;line-height:1;padding-top:8px}
.send{position:absolute;left:0;top:209px;width:109px;height:31px;border-radius:16px;background:var(--pink-deep);color:var(--white);font-size:8.6px;display:flex;align-items:center;justify-content:center}
.site-footer{position:absolute;left:0;top:929px;width:1035px;height:271px;background:var(--pink-soft);color:var(--white)}
.col{position:absolute;top:44px;width:160px}
.col h3{font-size:10px;font-weight:400;margin-bottom:26px}
.col p,.col li{font-size:7.5px;line-height:13.4px;list-style:none;color:#fbe3ef}
.social{position:absolute;left:175px;top:139px;display:flex;gap:9px}
.social span{width:26px;height:26px;border-radius:50%;background:#ec7db8}
.reach{position:absolute;left:701px;top:85px}
.reach-row{position:relative;padding-left:21px;font-size:7.5px;line-height:11px;color:#fbe3ef;margin-bottom:14px}
.reach-row svg{position:absolute;left:0;top:1px}
.copyright{position:absolute;left:0;width:100%;top:206px;text-align:center;font-size:7.5px;color:#fbe3ef}
</style>
</head>
<body>
<div class="hero" role="img" aria-label="Photo of the costume workshop with sewing tables and rails of dresses, under a pink triangle overlay"></div>

<header class="site-header">
  <div class="brand"><span class="brand-dot"></span>Glintora</div>
  <nav class="main-nav">
    <a class="current" style="left:603px">Home</a>
    <a style="left:645px">About Glintora</a>
    <a style="left:718px">Products</a>
    <a style="left:769px">Services</a>
    <a style="left:818px">Contact</a>
  </nav>
</header>

<h1 class="hero-title">CONTACT</h1>
<div class="breadcrumb"><b>HOME</b><span>CONTACT</span></div>

<h2 class="section-title">Contact Information</h2>
<p class="info" style="left:175px">Address: <strong>New Street 12345 123 St City, CANADA</strong></p>
<p class="info" style="left:351px">Phone: <strong>+ 5555 5555 55</strong></p>
<p class="info" style="left:526px">Email: <strong>info@yoursite.com</strong></p>
<p class="info" style="left:701px">Website <strong>yoursite.com</strong></p>

<div class="map" role="img" aria-label="Map showing the studio location"></div>

<form class="contact-form">
  <div class="field">Your Name</div>
  <div class="field">Your Email</div>
  <div class="field">Subject</div>
  <div class="field message">Message</div>
  <div class="send">Send Message</div>
</form>

<footer class="site-footer">
  <div class="col" style="left:175px">
    <h3>Glintora</h3>
    <p>Sales professional Luxury Goods. Development of jewelry product lines. Graduate Gemologist, Norvale Gem Institute.</p>
  </div>
  <div class="social"><span></span><span></span></div>
  <div class="col" style="left:363px">
    <h3>Development</h3>
    <ul><li>Private label</li><li>OEM</li><li>Startup</li></ul>
  </div>
  <div class="col" style="left:526px">
    <h3>Production</h3>
    <ul><li>Capabilities</li><li>Plating</li><li>Metal</li><li>Partners</li></ul>
  </div>
  <div class="col" style="left:701px"><h3>Have a Questions?</h3></div>
  <div class="reach">
    <div class="reach-row">
      <svg width="7" height="10" viewBox="0 0 7 10"><path d="M3.5 0A3.5 3.5 0 0 0 0 3.5C0 6 3.5 10 3.5 10S7 6 7 3.5A3.5 3.5 0 0 0 3.5 0zm0 5a1.4 1.4 0 1 1 0-2.8 1.4 1.4 0 0 1 0 2.8z" fill="#fff"/></svg>
      Larkfield Lane 18, 40211<br>Ostbrück, Germany
    </div>
    <div class="reach-row">
      <svg width="8" height="8" viewBox="0 0 8 8"><path d="M1.6 0l1.4 1.8-.8 1.1a5 5 0 0 0 2.9 2.9l1.1-.8L8 6.4 7 8C3.2 8 0 4.8 0 1z" fill="#fff"/></svg>
      +5555555555
    </div>
    <div class="reach-row" style="margin-top:16px">
      <svg width="10" height="7" viewBox="0 0 10 7"><rect width="10" height="7" fill="#fff"/><path d="M0 0l5 4 5-4" stroke="#e96aad" stroke-width="1" fill="none"/></svg>
      info@yourdomain.com
    </div>
  </div>
  <p class="copyright">Copyright ©2021 All rights reserved by Glintora</p>
</footer>
</body>
</html>
```